Beauty website banner

We are an Australian beauty website selling mid and high end cosmetics and beauty products.

We need a banner that tells customers they can share their product wishlists with friends to let them know what they want for Christmas.

Target Market(s)

Female, 30-60, white collar

Industry/Entity Type

Cosmetics

Requirements
Must have
• 600 x 150 pixels in size

Words to be as follows, not including the (") of course.

"Share your wishlist with friends and family for Christmas!"

(Then in smaller font) "Just log in to your account, go to your wishlist and click on the ‘share wishlist’ button"

```html
<!DOCTYPE html>
<html lang="en">
<head>
<meta charset="utf-8">
<title>Share your wishlist for Christmas</title>
<link href="https://fonts.googleapis.com/css2?family=Arvo:wght@400;700&display=swap" rel="stylesheet">
<style>
  :root {
    --red-light: #f3625f;
    --red-mid: #e8423f;
    --red-deep: #c9262a;
    --panel-red: #c8272b;
    --panel-red-dark: #a81b20;
    --white: #ffffff;
    --shadow: rgba(90, 0, 0, 0.55);
    --fold: #e9d3d3;
  }
  * { margin: 0; padding: 0; box-sizing: border-box; }
  html, body {
    width: 1200px;
    height: 300px;
    overflow: hidden;
    background: var(--white);
  }
  .banner {
    position: relative;
    width: 1200px;
    height: 300px;
    overflow: hidden;
    background: linear-gradient(180deg, var(--red-light) 0%, var(--red-mid) 55%, var(--red-deep) 100%);
  }
  .banner__pattern {
    position: absolute;
    inset: 0;
    background: radial-gradient(ellipse at 30% 40%, rgba(255,255,255,0.12), rgba(255,255,255,0) 70%);
  }
  .headline {
    position: absolute;
    left: 38px;
    top: 0;
    font-family: "Arvo", Georgia, serif;
    color: var(--white);
    text-shadow: 2px 3px 3px var(--shadow);
    line-height: 1;
  }
  .headline__line {
    position: absolute;
    left: 0;
    white-space: nowrap;
    font-weight: 400;
  }
  .headline__line--first { top: 36px; font-size: 60px; letter-spacing: 0.5px; }
  .headline__line--second { top: 116px; font-size: 49px; letter-spacing: 0.5px; }
  .headline__line--third { top: 186px; font-size: 72px; }
  .headline__holiday {
    font-size: 88px;
    font-weight: 700;
    color: var(--panel-red);
    -webkit-text-stroke: 8px var(--white);
    paint-order: stroke fill;
    margin-left: 6px;
    letter-spacing: 1px;
  }
  .steps {
    position: absolute;
    left: 776px;
    top: 22px;
    width: 400px;
    height: 258px;
  }
  .steps__frame {
    position: absolute;
    inset: 0;
  }
  .steps__list {
    position: absolute;
    left: 26px;
    top: 48px;
    list-style: none;
    font-family: Arial, Helvetica, sans-serif;
    font-size: 29px;
    color: var(--white);
    line-height: 1.3;
  }
  .steps__item {
    position: relative;
    padding-left: 20px;
    margin-bottom: 17px;
    text-shadow: 1px 1px 2px rgba(80,0,0,0.4);
  }
  .steps__item::before {
    content: "";
    position: absolute;
    left: 0;
    top: 13px;
    width: 12px;
    height: 12px;
    border-radius: 50%;
    background: var(--white);
  }
  .steps__item strong { font-weight: 700; }
</style>
</head>
<body>
  <div class="banner">
    <div class="banner__pattern"></div>

    <h1 class="headline">
      <span class="headline__line headline__line--first">Share your wishlist</span>
      <span class="headline__line headline__line--second">with friends and family</span>
      <span class="headline__line headline__line--third">for<span class="headline__holiday">Christmas!</span></span>
    </h1>

    <aside class="steps">
      <svg class="steps__frame" width="400" height="258" viewBox="0 0 400 258">
        <defs>
          <linearGradient id="panelFill" x1="0" y1="0" x2="0" y2="1">
            <stop offset="0" stop-color="#cf2f33"/>
            <stop offset="1" stop-color="#a81b20"/>
          </linearGradient>
        </defs>
        <path d="M14 4 H356 L396 44 V244 Q396 254 386 254 H14 Q4 254 4 244 V14 Q4 4 14 4 Z"
              fill="url(#panelFill)" stroke="#ffffff" stroke-width="5"/>
        <path d="M356 4 V36 Q356 44 364 44 H396 Z" fill="#e9d3d3" stroke="#ffffff" stroke-width="3"/>
      </svg>
      <ul class="steps__list">
        <li class="steps__item"><strong>Log in</strong> to your account</li>
        <li class="steps__item">Go to <strong>your wishlist</strong></li>
        <li class="steps__item">Click on the <strong>‘share<br>wishlist’</strong> button!</li>
      </ul>
    </aside>
  </div>
</body>
</html>
```